Company Banner

I would like our 5 corporate Core Values placed on a single banner that has a theme related to our engineering industry.

Core Values: Productive & Hard Working, Professional, Humble, Personable, Adaptable

Target Market(s)

Construction, Engineering

Requirements
Must have
• All words randomly positioned on the banner with color and industry background images.

Please add company logo to upper left corner as well (attached logo design file)

```html
<!DOCTYPE html>
<html lang="en">
<head>
<meta charset="utf-8">
<title>Company Core Values Banner</title>
<link rel="stylesheet" href="https://fonts.googleapis.com/css2?family=Arimo:wght@700&family=Barlow:wght@500&display=swap">
<style>
  :root {
    --page-bg: #ffffff;
    --steel-light: #9fb6c8;
    --steel-mid: #4f6f86;
    --steel-dark: #1d2c38;
    --furnace-glow: #d89a5a;
    --slate: #3f5863;
    --night: #050708;
    --lime: #c3d94a;
    --lime-soft: #d6e86a;
    --value-text: #f3f6c4;
    --value-edge: #2c3a12;
    --logo-panel: rgba(255, 255, 255, 0.86);
    --logo-ink: #3a3d40;
  }
  html, body {
    margin: 0;
    width: 1200px;
    height: 1200px;
    overflow: hidden;
    background: var(--page-bg);
  }
  .canvas {
    position: relative;
    width: 1200px;
    height: 1200px;
  }
  .banner {
    position: absolute;
    left: 58px;
    top: 385px;
    width: 1080px;
    height: 468px;
    overflow: hidden;
  }
  .banner svg {
    display: block;
    width: 1080px;
    height: 468px;
  }
  .brand-tab {
    position: absolute;
    left: 0;
    top: 26px;
    width: 384px;
    height: 57px;
    background: var(--logo-panel);
    display: flex;
    align-items: center;
    padding-left: 50px;
    box-sizing: border-box;
  }
  .brand-name {
    font-family: "Barlow", sans-serif;
    font-weight: 500;
    font-size: 30px;
    letter-spacing: 0.5px;
    color: var(--logo-ink);
    white-space: nowrap;
  }
  .core-value {
    font-family: "Arimo", sans-serif;
    font-weight: 700;
    font-size: 36px;
    letter-spacing: -1.2px;
    fill: var(--value-text);
    stroke: var(--value-edge);
    stroke-width: 1.2px;
    paint-order: stroke;
  }
  .value-rule {
    stroke: var(--lime);
    stroke-width: 2.5;
  }
</style>
</head>
<body>
<main class="canvas">
  <section class="banner">
    <svg viewBox="0 0 1080 468" xmlns="http://www.w3.org/2000/svg">
      <defs>
        <linearGradient id="plant-photo" x1="0" y1="0" x2="1" y2="1">
          <stop offset="0" stop-color="var(--steel-light)"/>
          <stop offset="0.3" stop-color="var(--furnace-glow)"/>
          <stop offset="0.55" stop-color="var(--steel-mid)"/>
          <stop offset="1" stop-color="var(--steel-dark)"/>
        </linearGradient>
        <linearGradient id="welding-photo" x1="0" y1="0" x2="1" y2="1">
          <stop offset="0" stop-color="var(--slate)"/>
          <stop offset="0.55" stop-color="#26363d"/>
          <stop offset="1" stop-color="var(--night)"/>
        </linearGradient>
        <linearGradient id="lime-sweep" x1="0" y1="0" x2="0" y2="1">
          <stop offset="0" stop-color="var(--lime)"/>
          <stop offset="1" stop-color="var(--lime-soft)"/>
        </linearGradient>
      </defs>

      <rect class="plant-photo" x="0" y="0" width="1080" height="468" fill="url(#plant-photo)"
            role="img" aria-label="Photo of industrial plant piping, valves and pressure gauges"/>

      <path class="lime-sweep" d="M668,0 L700,0 Q640,300 440,468 L358,468 Q590,300 668,0 Z" fill="url(#lime-sweep)"/>

      <path class="values-panel" d="M700,0 L1080,0 L1080,468 L440,468 Q640,300 700,0 Z" fill="url(#welding-photo)"
            role="img" aria-label="Photo of a welder at work with a shower of sparks"/>

      <text class="core-value" x="1011" y="76" text-anchor="end">Productive</text>
      <text class="core-value" x="1011" y="124" text-anchor="end">&amp; Hard Working</text>
      <line class="value-rule" x1="702" y1="141" x2="1023" y2="141"/>
      <text class="core-value" x="1011" y="188" text-anchor="end">Profesional</text>
      <line class="value-rule" x1="662" y1="219" x2="1023" y2="219"/>
      <text class="core-value" x="1011" y="268" text-anchor="end">Humble</text>
      <line class="value-rule" x1="615" y1="295" x2="1023" y2="295"/>
      <text class="core-value" x="1011" y="346" text-anchor="end">Personalble</text>
      <line class="value-rule" x1="567" y1="373" x2="1023" y2="373"/>
      <text class="core-value" x="1011" y="422" text-anchor="end">Adaptable</text>
    </svg>

    <div class="brand-tab">
      <span class="brand-name">RIDGEWAY BUILDERS</span>
    </div>
  </section>
</main>
</body>
</html>
```